One page website

I'm looking for a landing page for my company. Just a brief description of our medical device technology with some images

Coding

Coded - Design and coding required

```html
<!DOCTYPE html>
<html lang="en">
<head>
<meta charset="utf-8">
<title>Veritas Spine – Solving Children's Scoliosis</title>
<link href="https://fonts.googleapis.com/css2?family=Heebo:wght@300;400;500;700&family=Poppins:wght@400;500;600&display=swap" rel="stylesheet">
<style>
:root{
  --green:#8dc63f;
  --teal:#3bb4c9;
  --ink:#1d1d1d;
  --text:#333;
  --muted:#666;
  --soft:#f7f7f7;
  --line:#e6e6e6;
  --footer:#242424;
  --footer-text:#9a9a9a;
  --blue:#1e9ad6;
  --nav-blue:#2b8fd6;
}
*{box-sizing:border-box;margin:0;padding:0}
html,body{width:1200px;height:2901px;overflow:hidden}
body{position:relative;background:#fff;font-family:'Heebo',sans-serif;color:var(--text)}

/* header */
.site-header{position:absolute;left:0;top:0;width:1200px;height:83px;background:#fff;box-shadow:0 2px 6px rgba(0,0,0,.06);z-index:3}
.brand{position:absolute;left:118px;top:28px;display:flex;align-items:center;gap:8px;font-family:'Poppins',sans-serif;font-weight:500;font-size:20px;color:var(--green)}
.brand-dot{width:12px;height:12px;border-radius:50%;background:var(--green)}
.nav a{position:absolute;top:32px;font-size:18px;color:#333;text-decoration:none;font-weight:400}
.nav a.active{color:var(--nav-blue);font-weight:500;border-bottom:2px solid var(--nav-blue);padding-bottom:4px}
.btn-pill{position:absolute;display:flex;align-items:center;justify-content:center;background:var(--green);color:#fff;border-radius:20px;font-family:'Poppins',sans-serif}
.cta{left:921px;top:25px;width:162px;height:37px;font-size:15px;font-weight:500}

/* hero */
.hero-visual{position:absolute;left:0;top:83px;width:1200px;height:520px;background:linear-gradient(90deg,#f2f4f6 0%,#eaeef2 45%,#dde5ee 70%,#d3dce6 100%);clip-path:polygon(0 0,100% 0,100% 480px,600px 520px,0 480px)}
.hero-title{position:absolute;left:164px;top:176px;font-family:'Heebo',sans-serif}
.hero-title .kicker{display:block;font-size:80px;font-weight:700;color:var(--green);line-height:1}
.hero-title .main{display:block;font-size:59px;font-weight:300;color:#111;line-height:1;margin-top:8px}
.hero-sub{position:absolute;left:164px;top:352px;font-size:18px;color:#222}
.learn{left:162px;top:414px;width:161px;height:37px;font-size:16px}
.slider-arrow{position:absolute;top:281px;width:52px;height:43px;background:#fff;display:flex;align-items:center;justify-content:center;color:var(--teal);font-size:16px}

/* what we do */
.band-grey{position:absolute;left:0;width:1200px;background:var(--soft)}
.section-title{position:absolute;left:0;width:1200px;text-align:center;font-family:'Heebo',sans-serif}
.wwd-title{top:648px;font-size:43px;font-weight:700;color:#111}
.wwd-title span{color:var(--green);font-weight:400}
.wwd-text{position:absolute;top:716px;left:0;width:1200px;text-align:center;font-size:18px;line-height:30px;color:#222}
.card{position:absolute;top:843px;width:263px;height:249px;background:#fff;border:1px solid #ececec;border-radius:4px;box-shadow:0 2px 6px rgba(0,0,0,.05);text-align:center;font-family:'Poppins',sans-serif}
.card.featured{background:var(--green);border-color:var(--green);color:#fff}
.card svg{display:block;margin:26px auto 0}
.card h3{font-size:16px;font-weight:600;color:#111;margin-top:14px}
.card p{font-size:12px;line-height:21px;color:#555;margin-top:10px}
.card .more{display:block;font-size:12px;color:#444;margin-top:14px}
.card.featured h3,.card.featured p,.card.featured .more{color:#fff}

/* benefits */
.bene-title{font-size:32px;font-weight:700;color:#111;letter-spacing:-.5px}
.bene-item{position:absolute;display:flex;align-items:center;font-family:'Poppins',sans-serif;font-size:17px;line-height:30px;color:#222}
.bene-item svg{flex:none}
.photo{position:absolute}

/* team */
.team-title{top:2248px;font-size:34px;font-weight:400;color:#222;letter-spacing:1px}
.member-ring{position:absolute;width:86px;height:86px;border-radius:50%;border:3px solid var(--green);padding:5px}
.member-ring .avatar{width:100%;height:100%;border-radius:50%;background:linear-gradient(160deg,#c9d3df,#7f8ea3)}
.member{position:absolute;font-family:'Heebo',sans-serif;font-size:11.5px;line-height:14px;color:#444}
.member .name{font-size:15px;font-weight:700;color:#111;line-height:18px}
.member .role{font-size:15px;color:var(--nav-blue);line-height:17px;margin-bottom:6px}
.member p+p{margin-top:6px}
.dot{position:absolute;top:2524px;width:12px;height:12px;border-radius:50%;background:#ccc}
.dot.on{background:var(--green)}

/* footer */
.site-footer{position:absolute;left:0;top:2608px;width:1200px;height:293px;background:var(--footer);color:var(--footer-text);font-size:14px}
.site-footer h4{position:absolute;top:57px;font-size:16px;font-weight:400;color:#fff}
.site-footer .col{position:absolute;line-height:26px}
.divider{position:absolute;top:55px;width:1px;height:140px;background:#3a3a3a}
.email{position:absolute;left:661px;top:144px;width:418px;height:38px;border-radius:19px;background:#fff;overflow:hidden;display:flex}
.email span{flex:1;padding:10px 25px;color:#999;font-size:14px}
.email b{width:128px;background:var(--blue);color:#fff;display:flex;align-items:center;justify-content:center;font-weight:600;font-size:15px}
.copy{position:absolute;left:0;top:229px;width:1200px;border-top:1px solid #363636;padding-top:22px;text-align:center;font-size:14px}
</style>
</head>
<body>

<header class="site-header">
  <div class="brand"><span class="brand-dot"></span>Veritas Spine</div>
  <nav class="nav">
    <a class="active" style="left:457px">Home</a>
    <a style="left:563px">About</a>
    <a style="left:668px">Services</a>
    <a style="left:789px">Treatment</a>
  </nav>
  <a class="btn-pill cta">Get In Touch</a>
</header>

<section class="hero">
  <div class="hero-visual" role="img" aria-label="Girl stretching over an exercise ball in a bright therapy room"></div>
  <div class="slider-arrow" style="left:87px">&#8249;</div>
  <div class="slider-arrow" style="left:1062px">&#8250;</div>
  <h1 class="hero-title"><span class="kicker">SOLVING</span><span class="main">Children’s Scoliosis</span></h1>
  <p class="hero-sub">Develop novel technologies focusing on non-fusion scoliosis</p>
  <a class="btn-pill learn">Learn More</a>
</section>

<div class="band-grey" style="top:994px;height:659px"></div>

<section class="what-we-do">
  <h2 class="section-title wwd-title">What <span>We Do</span></h2>
  <p class="wwd-text">Develop novel technologies focusing on non-fusion scoliosis correction allowing for<br>non-surgical dynamic adjustment of implants over time.</p>

  <div class="card" style="left:179px">
    <svg width="70" height="68" viewBox="0 0 70 68" fill="none" stroke="var(--teal)" stroke-width="2"><circle cx="44" cy="8" r="6"/><path d="M6 34h58v10H6z"/><path d="M10 44v20M60 44v20M30 44v20M40 44v20"/><path d="M20 34c4-10 14-14 24-12"/></svg>
    <h3>Monitoring Treatment</h3>
    <p>Lorem Ipsum is simply dummy<br>and typesetting</p>
    <span class="more">Read More &nbsp;›</span>
  </div>
  <div class="card featured" style="left:469px">
    <svg width="70" height="68" viewBox="0 0 70 68" fill="none" stroke="#fff" stroke-width="2"><path d="M35 4v60"/><rect x="29" y="10" width="12" height="8" rx="3"/><rect x="29" y="22" width="12" height="8" rx="3"/><rect x="29" y="34" width="12" height="8" rx="3"/><rect x="29" y="46" width="12" height="8" rx="3"/><path d="M22 6c-8 6-10 20-4 30M48 6c8 6 10 20 4 30"/></svg>
    <h3>Bracing Treatment</h3>
    <p>Lorem Ipsum is simply dummy<br>and typesetting</p>
    <span class="more">Read More &nbsp;›</span>
  </div>
  <div class="card" style="left:759px">
    <svg width="70" height="68" viewBox="0 0 70 68" fill="none" stroke="var(--teal)" stroke-width="2"><circle cx="35" cy="12" r="8"/><path d="M6 22l20 10h18l20-10M26 32v10h18V32"/><path d="M4 50c8-5 14 5 22 0s14 5 22 0 14 5 18 0M4 60c8-5 14 5 22 0s14 5 22 0 14 5 18 0"/></svg>
    <h3>Fusion Treatment</h3>
    <p>Lorem Ipsum is simply dummy<br>and typesetting</p>
    <span class="more">Read More &nbsp;›</span>
  </div>
</section>

<section class="benefits-advantages">
  <h2 class="section-title bene-title" style="top:1198px">BENEFITS - ADVANTAGES OF VBT OVER FUSION</h2>
  <div class="bene-item" style="left:242px;top:1279px"><svg width="50" height="48" viewBox="0 0 50 48" fill="none" stroke="var(--teal)" stroke-width="2"><path d="M4 44h42M8 44V32h6v12M20 44V24h6v20M32 44V16h6v28M6 26L38 4M30 4h8v8"/></svg><span style="margin-left:24px">Continued skeletal growth</span></div>
  <div class="bene-item" style="left:242px;top:1355px"><svg width="50" height="52" viewBox="0 0 50 52" fill="none" stroke="var(--teal)" stroke-width="2"><circle cx="12" cy="8" r="5"/><path d="M6 4v40M4 30h42v8H4M10 38v10M42 38v10M16 26h26"/></svg><span style="margin-left:24px">Single treatment event</span></div>
  <div class="bene-item" style="left:236px;top:1433px"><svg width="56" height="52" viewBox="0 0 56 52" fill="none" stroke="var(--teal)" stroke-width="2"><circle cx="44" cy="8" r="5"/><path d="M4 22l14-8 10 6 8-8M28 20l-6 14 10 6-4 10M22 34l-10 14"/></svg><span style="margin-left:18px">Partial Motion Preservation</span></div>
  <div class="bene-item" style="left:242px;top:1514px;align-items:flex-start"><svg width="50" height="52" viewBox="0 0 50 52" fill="none" stroke="var(--teal)" stroke-width="2"><circle cx="8" cy="6" r="4"/><circle cx="42" cy="6" r="4"/><path d="M8 12v38M42 12v38M14 22h22v20H14zM20 22v-6h10v6"/></svg><span style="margin-left:24px">Little impact on activity<br>and appearance</span></div>
  <div class="photo" style="left:638px;top:1290px;width:325px;height:287px;background:linear-gradient(135deg,#dde1e6,#c8ced6)" role="img" aria-label="Boy in a white T-shirt sitting on an exam table while a clinician checks his shoulders"></div>
</section>

<section class="benefits-results">
  <h2 class="section-title bene-title" style="top:1715px">BENEFITS - VBT HAS PROVEN RESULTS</h2>
  <div class="photo" style="left:226px;top:1813px;width:326px;height:287px;background:linear-gradient(160deg,#eef0f2,#b9bdc2)" role="img" aria-label="Girl balancing on a grey exercise ball during a physiotherapy session"></div>
  <div class="bene-item" style="left:646px;top:1806px;align-items:flex-start"><svg width="52" height="56" viewBox="0 0 52 56" fill="none" stroke="var(--teal)" stroke-width="2"><circle cx="28" cy="20" r="11"/><path d="M28 14v12M25 17h5M2 40h14l10 4h16l6-6M2 52h20l16-6"/><path d="M28 2v4M20 4l2 3M36 4l-2 3"/></svg><span style="margin-left:12px">~66% Cost Savings ($50K<br>compared to $150K)</span></div>
  <div class="bene-item" style="left:648px;top:1890px;align-items:flex-start"><svg width="50" height="52" viewBox="0 0 50 52" fill="none" stroke="var(--teal)" stroke-width="2"><circle cx="12" cy="8" r="5"/><path d="M6 4v40M4 30h42v8H4M10 38v10M42 38v10M16 26h26"/></svg><span style="margin-left:12px">50% Saving in Hospital Stay<br>(2-3 days compared to 6-7 days)</span></div>
  <div class="bene-item" style="left:638px;top:1971px;align-items:flex-start"><svg width="54" height="52" viewBox="0 0 54 52" fill="none" stroke="var(--teal)" stroke-width="2"><circle cx="27" cy="18" r="14"/><path d="M27 10v8l6 4M4 24l6 18 10 6M50 24l-6 18-10 6"/></svg><span style="margin-left:22px">50% Saving in Surgery Time<br>(1.5-2 hrs compared to 4-6 hrs)</span></div>
  <div class="bene-item" style="left:638px;top:2053px;align-items:flex-start"><svg width="54" height="52" viewBox="0 0 54 52" fill="none" stroke="var(--teal)" stroke-width="2"><path d="M8 18a22 22 0 0 1 38-4M46 34a22 22 0 0 1-38 4"/><path d="M18 24h6v16h-6zM24 38h14l3-10h-9l2-8-5-2-5 8"/></svg><span style="margin-left:22px">Confirmed improved self-<br>confidence for surgical recipients</span></div>
</section>

<div class="band-grey" style="top:2184px;height:424px"></div>

<section class="team">
  <h2 class="section-title team-title">OUR TEAM</h2>

  <div class="member-ring" style="left:156px;top:2335px"><div class="avatar" role="img" aria-label="Portrait of Daniel Hartley"></div></div>
  <div class="member" style="left:260px;top:2334px;width:140px">
    <div class="name">Daniel Hartley</div>
    <div class="role">Founder and CEO</div>
    <p>Co-founder and CEO<br>of AxisForm Labs.<br>Acquired by Northline<br>in 2014</p>
    <p>Leadership positions at<br>Calder Health and Pemberly</p>
  </div>

  <div class="member-ring" style="left:462px;top:2335px"><div class="avatar" role="img" aria-label="Portrait of Arjun Mehra"></div></div>
  <div class="member" style="left:565px;top:2334px;width:150px">
    <div class="name">Arjun Mehra Ph.D.</div>
    <div class="role">Co-Founder Chief<br>Science Officer</div>
    <p>Previous Chief Science<br>Officer at AxisForm<br>Labs</p>
    <p>Previous leadership<br>positions at Spinewell,<br>Northline and Orthovia</p>
  </div>

  <div class="member-ring" style="left:795px;top:2335px"><div class="avatar" role="img" aria-label="Portrait of Arjun Mehra"></div></div>
  <div class="member" style="left:897px;top:2334px;width:150px">
    <div class="name">Arjun Mehra Ph.D.</div>
    <div class="role">Co-Founder Chief<br>Science Officer</div>
    <p>Previous Chief Science<br>Officer at AxisForm<br>Labs</p>
    <p>Previous leadership<br>positions at Spinewell,<br>Northline and Orthovia</p>
  </div>

  <span class="dot" style="left:566px"></span>
  <span class="dot on" style="left:594px"></span>
  <span class="dot" style="left:621px"></span>
</section>

<footer class="site-footer">
  <h4 style="left:118px">Contact Us</h4>
  <div class="col" style="left:118px;top:94px;line-height:22px">Lorem Ipsum,<br>is simply dummy text of</div>
  <div class="col" style="left:118px;top:150px">xxx xxx xxxx</div>
  <div class="col" style="left:118px;top:181px">xxxxxxx@mailbox.com</div>
  <span class="divider" style="left:332px"></span>
  <h4 style="left:415px">Contact Us</h4>
  <div class="col" style="left:415px;top:92px">Home<br>About<br>Services<br>Contact</div>
  <span class="divider" style="left:575px"></span>
  <h4 style="left:662px">Email Newsletters</h4>
  <div class="col" style="left:662px;top:92px">Keep me up to date with content, updates, and offers from brightpath</div>
  <div class="email"><span>Email address</span><b>Subscribe</b></div>
  <div class="copy">Copyright Veritas Spine. All right reserved.</div>
</footer>

</body>
</html>
```